High end Natural/Therapeutic, skin care company needs packaging design

We need packaging designs for a line of natural cream deodorants made in Canada. They will be launched in retail spas and health stores this fall.
Our company formulates effective, pretty products bought mainly by women ages 35 to 75. These are top shelf products that deliver exceptional value for their cost.
Our company name is "Copper Lantern". We would like Natural Skin Care incorporated as well. The company name should be prominent, legible, duplicatable and recognizable through each product. The product "Deodorant" should be the most prominent. The customer should be able to pick that out easily.
The overall feel of the name and packaging should be feminine, but not frilly. Upscale but not uppity. These are common sense products that make the person feel good about themselves when they see, touch and use them. Each product should have it's own identity, but still have Copper Lantern, Natural Skin Care as the recognizable source.
Our packaging for the deodorants is in clear glass 60 mL jars (55mm height X 55mm diameter, label that goes around it is 1" width X maximum of 6.5" long. Circular label on the top of the lid is 1.67". Information on it is Copper Lantern Natural Skin care and around that is Reveal your true beauty, naturally.) The jar is in a printed box.
The box is 2.5 inches X 2.5 inches X 2.5 inches. No windows in the box.
Solvane Deodorant cream #1, is Sensitive with Lavender as the main essential oil
fragrance. This package should have the feeling of lightness, airiness and femininity. Solvane Deodorant cream #2 is Extra Strength, with Citrus essential oils as the scent. It should have brighter, bolder colors with a slightly masculine feel.
If you leave room for the directions, ingredients and description, I will fill in the body of the information later. Mainly what I am looking for is the font for the name and product and the artistry and color of your designs.
As well as deodorant, Copper Lantern formulates several therapeutic, pain remedies and face serums, toner, and creams. These products use strong, innovative natural ingredients that work for delicate, thin skinned, sensitive skin types. Whenever possible we incorporate Dead Sea minerals from Israel into our products.
Target Market(s)
Women ages 35 to 75
Industry/Entity Type
It Company
Requirements
Must have
- name: COPPER LANTERN Natural Skin Care
Reveal your true beauty, naturally
#1 Solvane Deodorant cream, Sensitive, Lavender
#2 Solvane Deodorant cream Extra Strength, Citrus
Nice to have
- The logo below is what I have been using, but would like to change it. I would like it to look more upscale, bolder, less script. Possibly use Trajan Pro 3 for Copper Lantern and a script for Natural Skin care. As well, I do like the font that the Odette example uses.
I have uploaded some examples of packaging that I like. Hope this helps.
Should not have
- Cartoon, childlike characters. Please do not use the existing Copper Lantern logo, it is for reference only.

```html
<!DOCTYPE html>
<html lang="en">
<head>
<meta charset="utf-8">
<title>Copper Lantern – Solvane Deodorant Cream Box Fronts</title>
<link rel="stylesheet" href="https://fonts.googleapis.com/css2?family=Tinos:wght@400;700&family=Arimo:wght@400&family=Roboto+Condensed:wght@400;700&family=Handlee&display=swap">
<style>
  :root {
    --canvas: #f1f1f3;
    --white: #ffffff;
    --lav-top: #7e3f98;
    --lav-band: #d65aa2;
    --lav-strip: #7e3f98;
    --lav-photo-a: #b893c8;
    --lav-photo-b: #a67fb9;
    --cit-top: #f47d22;
    --cit-band: #9aa81d;
    --cit-strip: #f47d22;
    --cit-photo-a: #ffd04a;
    --cit-photo-b: #f9b21b;
  }
  * { margin: 0; padding: 0; box-sizing: border-box; }
  html, body {
    width: 1200px; height: 1000px; overflow: hidden;
    background: var(--canvas);
  }
  .canvas { position: relative; width: 1200px; height: 1000px; }

  .box-front {
    position: absolute; top: 307px;
    width: 385px; height: 383px;
    color: var(--white);
    overflow: hidden;
  }
  .box-front--lavender { left: 160px; }
  .box-front--citrus { left: 653px; }

  .brand-panel {
    position: absolute; left: 0; top: 0; width: 100%; height: 173px;
    text-align: center;
  }
  .box-front--lavender .brand-panel { background: var(--lav-top); }
  .box-front--citrus .brand-panel { background: var(--cit-top); }

  .brand-name {
    position: absolute; left: 0; right: 0; top: 40px;
    font-family: "Tinos", "Times New Roman", serif;
    font-weight: 400; font-size: 35px; letter-spacing: 0.5px; line-height: 1;
  }
  .brand-line {
    position: absolute; left: 46px; right: 46px; top: 80px;
    display: flex; align-items: center; gap: 10px;
    font-family: "Arimo", Arial, sans-serif;
    font-size: 14px; letter-spacing: 0.8px; white-space: nowrap;
  }
  .brand-line::before, .brand-line::after {
    content: ""; flex: 1; height: 1px; background: var(--white);
  }
  .tagline {
    position: absolute; left: 0; right: 0; top: 118px;
    font-family: "Handlee", cursive;
    font-size: 18px; line-height: 1;
  }

  .product-band {
    position: absolute; left: 0; top: 173px; width: 100%; height: 38px;
    display: flex; align-items: center; justify-content: center;
    font-family: "Tinos", "Times New Roman", serif;
    font-weight: 700; font-size: 17px; letter-spacing: 0.3px;
  }
  .box-front--lavender .product-band { background: var(--lav-band); }
  .box-front--citrus .product-band { background: var(--cit-band); }

  .variant-strip {
    position: absolute; left: 0; top: 211px; width: 100%; height: 24px;
    display: flex; align-items: center; justify-content: center; gap: 6px;
    font-family: "Roboto Condensed", Arial, sans-serif; font-size: 14px;
  }
  .box-front--lavender .variant-strip { background: var(--lav-strip); }
  .box-front--citrus .variant-strip { background: var(--cit-strip); }
  .variant-strip strong { font-weight: 700; }

  .scent-photo {
    position: absolute; left: 0; top: 235px; width: 100%; height: 148px;
  }
  .box-front--lavender .scent-photo {
    background: linear-gradient(160deg, var(--lav-photo-a), var(--lav-photo-b));
  }
  .box-front--citrus .scent-photo {
    background: radial-gradient(circle at 50% 60%, #fff1b8 0%, var(--cit-photo-a) 35%, var(--cit-photo-b) 100%);
  }

  .volume {
    position: absolute; left: 0; right: 0; bottom: 10px;
    text-align: center;
    font-family: "Roboto Condensed", Arial, sans-serif;
    font-weight: 700; font-size: 14px;
  }
</style>
</head>
<body>
<main class="canvas">

  <section class="box-front box-front--lavender">
    <header class="brand-panel">
      <h1 class="brand-name">COPPER LANTERN</h1>
      <p class="brand-line">NATURAL SKIN CARE</p>
      <p class="tagline">Reveal your true beauty, naturally</p>
    </header>
    <h2 class="product-band">SOLVANE DEODORANT CREAM</h2>
    <p class="variant-strip"><strong>SENSITIVE</strong> | LAVENDER</p>
    <div class="scent-photo" role="img" aria-label="Soft-focus photograph of lavender sprigs in violet tones"></div>
    <p class="volume">60 ml</p>
  </section>

  <section class="box-front box-front--citrus">
    <header class="brand-panel">
      <h1 class="brand-name">COPPER LANTERN</h1>
      <p class="brand-line">NATURAL SKIN CARE</p>
      <p class="tagline">Reveal your true beauty, naturally</p>
    </header>
    <h2 class="product-band">SOLVANE DEODORANT CREAM</h2>
    <p class="variant-strip"><strong>EXTRA STRENGTH</strong> | CITRUS</p>
    <div class="scent-photo" role="img" aria-label="Close-up photograph of a citrus blossom in warm yellow tones"></div>
    <p class="volume">60 ml</p>
  </section>

</main>
</body>
</html>
```